Global Expert Network Firm needs business card design

We need business card design for a new company based in Seoul, South Korea called 'Corwell Insight Partners'. We recruit industry experts covering all countries and connect our client and recruited expert by phone, face-to-face meetings and etc. We are a global expert network firm that is focused on delivering high-quality experts to our clients throughout the world. Our clients include multinational corporations, global consulting firms, private equity firms, venture capital firms, asset management companies.
We have made new logo and please find attachment.(Please use new logo)
Target Market(s)
Global Consulting Firms, Investment Firms, Private Equity Firms, Venture Capital Firms.
Industry/Entity Type
Recruitment
Contact Information for Business Card
We need two Languages (English and Korean Version).
The front is Korean and the back is English version.
[The back] [English]
Company Name: Corwell Insight Partners, Inc.
CEO Name: Daniel Park
Address: #507, Hanbit Bldg, 82 Maebongsan-ro, Dobong-gu, Seoul, 01327, Korea
Tel. +82 2 718 4052
Fax. +82 2 864 1097
Mobile. +82 10 7264 8815
Email: daniel@corwellip.com
Web: www.corwellip.com
[The front] [Korean] => Described in same order as English version.
회사명: 코웰인사이트파트너스(주)
대표이사: 박도현
주소: 서울시 도봉구 매봉산로 82 한빛빌딩 507호
Tel. 02 718 4052
Fax. 02 864 1097
Mobile. 010 7264 8815
Web: www.corwellip.com
Look and feel
Each slider illustrates characteristics of the customer's brand and the style your logo design should communicate.

```html
<!DOCTYPE html>
<html lang="en">
<head>
<meta charset="utf-8">
<title>Corwell Insight Partners – Business Cards</title>
<link rel="stylesheet" href="https://fonts.googleapis.com/css2?family=Mulish:wght@300;400;600&family=Noto+Sans+KR:wght@300;400&display=swap">
<style>
  :root {
    --backdrop: #dedede;
    --paper: #e6e6e6;
    --navy: #1b1f4a;
    --ink-light: #eef0f6;
  }
  * { margin: 0; padding: 0; box-sizing: border-box; }
  html, body { width: 1200px; height: 965px; overflow: hidden; }
  body { background: var(--backdrop); font-family: "Mulish", sans-serif; position: relative; }

  .card {
    position: absolute; left: 277px; width: 648px; height: 370px;
    display: flex; background: var(--paper);
  }
  .card--english { top: 97px; }
  .card--korean { top: 502px; }

  .card__brand-side { position: relative; width: 321px; height: 100%; }
  .brand-block {
    position: absolute; left: 66px; top: 93px; width: 182px; height: 186px;
    background: var(--navy); color: var(--ink-light);
    padding: 22px 0 0 9px;
    font-family: "Mulish", sans-serif; font-weight: 300;
    font-size: 27px; line-height: 50px; letter-spacing: 0.5px;
    text-transform: uppercase;
  }

  .card__info-side {
    position: relative; width: 327px; height: 100%;
    background: var(--navy); color: var(--ink-light);
    padding-left: 37px;
  }
  .pointer { position: absolute; left: 0; top: 55px; width: 26px; height: 54px; }

  .person__name { position: absolute; top: 62px; font-size: 19.5px; font-weight: 600; letter-spacing: 0.2px; }
  .person__title { position: absolute; top: 86px; font-size: 14.5px; font-weight: 400; }
  .address { position: absolute; top: 130px; font-size: 14.5px; line-height: 19px; font-weight: 400; }

  .contacts { position: absolute; top: 208px; list-style: none; font-size: 14.5px; line-height: 19.7px; }
  .contacts li { display: flex; align-items: center; gap: 7px; }
  .contacts svg { width: 12px; height: 12px; flex: none; }

  .card--korean .person__name,
  .card--korean .person__title,
  .card--korean .address { font-family: "Noto Sans KR", sans-serif; font-weight: 300; }
  .card--korean .person__name { top: 58px; font-size: 19px; font-weight: 400; }
  .card--korean .person__title { top: 84px; font-size: 13.5px; }
  .card--korean .address { top: 138px; font-size: 14px; }
</style>
</head>
<body>

<svg width="0" height="0" style="position:absolute">
  <defs>
    <symbol id="icon-mobile" viewBox="0 0 12 12"><rect x="3" y="0.8" width="6" height="10.4" rx="1" fill="none" stroke="currentColor" stroke-width="1"/></symbol>
    <symbol id="icon-phone" viewBox="0 0 12 12"><path d="M2.3 1.2 4 0.8 5.2 3.3 4 4.3c.6 1.4 1.8 2.6 3.2 3.2l1-1.2 2.5 1.2-.4 1.7C9.8 10.3 8.7 11 7.6 10.7 4.6 9.8 2.2 7.4 1.3 4.4 1 3.3 1.6 2 2.3 1.2Z" fill="currentColor"/></symbol>
    <symbol id="icon-fax" viewBox="0 0 12 12"><rect x="3" y="0.8" width="6" height="3" fill="currentColor"/><rect x="1" y="4.2" width="10" height="4.5" rx="0.8" fill="currentColor"/><rect x="3" y="7.5" width="6" height="3.7" fill="none" stroke="currentColor" stroke-width="1"/></symbol>
    <symbol id="icon-mail" viewBox="0 0 12 12"><rect x="0.8" y="2.3" width="10.4" height="7.4" fill="none" stroke="currentColor" stroke-width="1"/><path d="M0.8 2.3 6 6.6l5.2-4.3M0.8 9.7 4.5 5.4M11.2 9.7 7.5 5.4" fill="none" stroke="currentColor" stroke-width="0.9"/></symbol>
    <symbol id="icon-web" viewBox="0 0 12 12"><g fill="none" stroke="currentColor" stroke-width="0.9"><circle cx="6" cy="6" r="5.1"/><ellipse cx="6" cy="6" rx="2.3" ry="5.1"/><path d="M0.9 6h10.2M1.8 3.4h8.4M1.8 8.6h8.4"/></g></symbol>
  </defs>
</svg>

<section class="card card--english" aria-label="English side">
  <div class="card__brand-side">
    <div class="brand-block">Corwell<br>Insight<br>Partners</div>
  </div>
  <div class="card__info-side">
    <svg class="pointer" viewBox="0 0 26 54" aria-hidden="true"><polygon points="0,0 26,27 0,54" fill="var(--paper)"/></svg>
    <p class="person__name">DANIEL PARK</p>
    <p class="person__title">CEO</p>
    <p class="address">#507, Hanbit Bldg,<br>82 Maebongsan-ro, Dobong-gu,<br>Seoul, 01327, Korea</p>
    <ul class="contacts">
      <li><svg><use href="#icon-mobile"/></svg>+82 2 718 4052</li>
      <li><svg><use href="#icon-phone"/></svg>+82 2 864 1097</li>
      <li><svg><use href="#icon-fax"/></svg>+82 10 7264 8815</li>
      <li><svg><use href="#icon-mail"/></svg>daniel@corwellip.com</li>
      <li><svg><use href="#icon-web"/></svg>www.corwellip.com</li>
    </ul>
  </div>
</section>

<section class="card card--korean" lang="ko" aria-label="Korean side">
  <div class="card__brand-side">
    <div class="brand-block" lang="en">Corwell<br>Insight<br>Partners</div>
  </div>
  <div class="card__info-side">
    <svg class="pointer" viewBox="0 0 26 54" aria-hidden="true"><polygon points="0,0 26,27 0,54" fill="var(--paper)"/></svg>
    <p class="person__name">박도현</p>
    <p class="person__title">대표이사</p>
    <p class="address">서울시 도봉구 매봉산로<br>82 한빛빌딩 507호</p>
    <ul class="contacts">
      <li><svg><use href="#icon-mobile"/></svg>+82 2 718 4052</li>
      <li><svg><use href="#icon-phone"/></svg>+82 2 864 1097</li>
      <li><svg><use href="#icon-fax"/></svg>+82 10 7264 8815</li>
      <li><svg><use href="#icon-mail"/></svg>daniel@corwellip.com</li>
      <li><svg><use href="#icon-web"/></svg>www.corwellip.com</li>
    </ul>
  </div>
</section>

</body>
</html>
```